Cat sitting business Web Design Project ***

I have a cat sitting business where I either take care of cats in their home or board them in mine

I need a website which offers my services, my rates, about me, FAQ's, Hours of operation and service areas covered, testimonials, contact info, newsletter sign up, gallery of photos and the ability for me to go in and update when needed.

Coded - Design and coding required

5+ page

```html
<!DOCTYPE html>
<html lang="en">
<head>
<meta charset="utf-8">
<title>Velvet Paws Cat Sitting</title>
<link href="https://fonts.googleapis.com/css2?family=Montserrat:wght@400;500;600;700;800;900&family=Raleway:wght@300;400;500;600;700&family=Open+Sans:wght@400;600&display=swap" rel="stylesheet">
<style>
:root{
  --brand-red:#a04544;
  --brand-red-dark:#8e3b3a;
  --brand-green:#7dbb42;
  --ink:#333333;
  --muted:#666666;
  --paper:#ffffff;
  --soft:#f1f1f1;
  --card:#e4e3e3;
  --footer:#a0564a;
  --footer-bar:#4a4a4a;
}
*{box-sizing:border-box;margin:0;padding:0}
html,body{width:1200px;height:5190px;overflow:hidden;background:var(--paper)}
body{position:relative;font-family:"Open Sans",sans-serif;color:var(--ink)}
.abs{position:absolute}
.section{position:absolute;left:0;width:1200px}

/* header */
.header{top:0;height:127px}
.brand{left:150px;top:26px;display:flex;align-items:center;gap:10px}
.brand-dot{width:38px;height:38px;border-radius:50%;border:2px solid var(--brand-green)}
.brand-name{font-family:"Raleway",sans-serif;font-weight:600;font-size:15px;color:var(--brand-red);line-height:1.2;width:110px}
.call{left:770px;top:46px;font-family:"Montserrat",sans-serif;font-weight:600;color:var(--brand-green);font-size:17px;line-height:1.15}
.call strong{display:block;color:var(--brand-red);font-size:19px}
.follow{left:968px;top:38px;font-family:"Montserrat",sans-serif;font-weight:600;color:var(--brand-green);font-size:16px;text-align:center}
.social{display:flex;gap:4px;margin-top:6px}
.social span{width:20px;height:20px;background:var(--brand-red);display:block}

.nav{top:127px;height:44px;background:var(--brand-red);display:flex;padding-left:112px}
.nav a{font-family:"Montserrat",sans-serif;font-weight:700;color:#fff;text-decoration:none;font-size:18px;line-height:44px;padding:0 32px;border-right:1px solid rgba(255,255,255,.35)}
.nav a:last-child{border-right:none}

/* hero */
.hero{top:171px;height:691px;background:linear-gradient(90deg,#f4f1ef 0%,#ece6e2 45%,#d9c8bd 70%,#c9b3a5 100%)}
.hero-title{left:62px;top:178px;font-family:"Montserrat",sans-serif;font-weight:900;font-size:66px;color:var(--brand-red);letter-spacing:1px;line-height:1}
.hero-sub{left:64px;top:244px;font-family:"Raleway",sans-serif;font-weight:400;font-size:64px;color:var(--brand-green);line-height:1}
.hero-copy{left:68px;top:325px;width:460px;font-size:13.5px;line-height:1.35;color:#444}
.btn-green{background:var(--brand-green);color:#fff;font-family:"Montserrat",sans-serif;font-weight:700;border-radius:6px;display:flex;align-items:center;gap:10px}
.hero-btn{left:64px;top:406px;height:40px;width:272px;padding:0 16px;font-size:16px}

/* about */
.about{top:862px;height:645px}
.about-photo{left:123px;top:89px;width:415px;height:492px;background:linear-gradient(160deg,#b89877,#8a6a52 55%,#5a4a44)}
.h-green{font-family:"Raleway",sans-serif;font-weight:500;color:var(--brand-green)}
.about-title{left:617px;top:92px;font-size:48px}
.rule{height:3px;width:62px;background:var(--brand-red)}
.about-rule{left:619px;top:156px}
.about-text{left:619px;top:186px;width:464px;font-size:12.5px;line-height:1.85;color:#555;text-align:justify}
.about-text p{margin-bottom:22px}
.pill{display:flex;align-items:center;justify-content:space-between;border-radius:12px;font-family:"Montserrat",sans-serif;font-weight:600;font-size:9px;color:#fff;padding:0 4px 0 14px;height:20px}
.pill i{width:14px;height:14px;border-radius:50%;background:#fff;display:block}
.about-more{left:619px;top:548px;width:110px;background:var(--brand-red)}

/* services */
.services{top:1507px;height:679px;background:var(--brand-red)}
.services-title{left:0;width:1200px;top:66px;text-align:center;font-family:"Raleway",sans-serif;font-size:48px;color:var(--brand-green)}
.services-title b{font-weight:700}
.services-rule{left:569px;top:138px;background:#fff}
.service{top:185px;width:330px;text-align:center;color:#fff}
.service-photo{width:196px;height:196px;border-radius:50%;border:5px solid #fff;margin:0 auto;background:linear-gradient(135deg,#cfd6d8,#8da2a8)}
.service h3{font-family:"Raleway",sans-serif;font-weight:500;font-size:26px;line-height:1.25;margin-top:16px}
.service h3 span{display:block;font-weight:400}
.service p{font-size:13px;line-height:1.35;margin-top:14px}
.service .pill{width:108px;margin:22px auto 0;background:var(--brand-green)}

/* faq */
.faq{top:2186px;height:594px}
.faq-title{left:0;width:1200px;top:68px;text-align:center;font-family:"Raleway",sans-serif;font-weight:700;font-size:34px;color:var(--brand-green)}
.faq-item{left:140px;width:928px;border-bottom:3px solid #555}
.faq-q{font-family:"Montserrat",sans-serif;font-weight:600;font-size:19px;color:var(--brand-red);display:flex;justify-content:space-between}
.faq-q span:last-child{color:var(--brand-red);font-weight:500;font-size:26px;line-height:19px}
.faq-a{font-size:12.5px;line-height:1.3;width:640px;margin-top:8px;color:#333}

/* rates */
.rates{top:2780px;height:746px;background:var(--brand-green)}
.rates-title{left:0;width:1200px;top:70px;text-align:center;font-family:"Raleway",sans-serif;font-size:36px;color:#fff}
.rates-title b{font-weight:700}
.rates-copy{left:140px;width:940px;top:160px;text-align:center;color:#fff;font-size:13px;line-height:1.35}
.plan{width:198px;height:360px;background:var(--card);border-radius:12px;overflow:hidden;text-align:center}
.plan-head{height:56px;background:var(--brand-red);color:#fff;font-family:"Montserrat",sans-serif;font-weight:600;font-size:27px;line-height:56px}
.plan-price{font-family:"Montserrat",sans-serif;font-weight:800;font-size:44px;color:var(--brand-red);margin-top:14px;line-height:1}
.plan-price sup{font-size:20px}
.plan-tag{font-family:"Montserrat",sans-serif;font-weight:700;font-size:13px;color:var(--brand-red);line-height:1.05;margin-top:6px}
.plan ul{list-style:none;text-align:left;margin:18px 0 0 26px;font-size:14px;line-height:30px;color:#333}
.plan li{display:flex;align-items:center;gap:8px}
.plan .pill{width:100px;margin:12px auto 0;background:var(--brand-green);font-size:12px;height:22px}

/* testimonials */
.testimonials{top:3526px;height:500px}
.t-title{left:0;width:1200px;top:66px;text-align:center;font-family:"Raleway",sans-serif;font-weight:600;font-size:34px;color:var(--brand-red)}
.t-rule{left:569px;top:126px;background:#333}
.quote{top:210px;width:320px}
.quote-mark{font-family:"Montserrat",sans-serif;font-weight:900;font-size:46px;color:var(--brand-red);line-height:.6}
.quote h4{font-family:"Montserrat",sans-serif;font-weight:600;font-size:15px;color:var(--brand-green);margin-top:14px}
.quote p{font-size:13px;line-height:1.45;color:#666;margin-top:10px;text-align:justify}
.quote .who{font-family:"Montserrat",sans-serif;font-weight:700;font-size:15px;color:var(--brand-green);margin:44px 0 0 12px}
.quote .role{font-size:12.5px;color:#666;margin-left:12px}

/* newsletter band */
.signup{top:4026px;height:74px;background:var(--brand-red)}
.signup-icon{left:218px;top:12px;width:48px;height:48px;border-radius:50%;background:var(--brand-green);border:4px solid #fff}
.signup-label{left:310px;top:19px;font-family:"Raleway",sans-serif;font-weight:500;font-size:27px;color:#fff}
.signup-input{left:612px;top:22px;width:354px;height:32px;background:#fff;font-size:12px;padding-left:24px;line-height:32px;color:#333}
.signup-btn{left:966px;top:22px;width:118px;height:32px;background:var(--brand-green);color:#fff;font-family:"Montserrat",sans-serif;font-size:13px;line-height:32px;text-align:center}

/* gallery */
.gallery{top:4100px;height:732px;background:linear-gradient(180deg,#f0efee,#e6e4e2)}
.g-title{left:0;width:1200px;top:88px;text-align:center;font-family:"Montserrat",sans-serif;font-weight:600;font-size:30px;color:var(--brand-red)}
.g-rule{left:569px;top:136px;background:#333}
.g-photo{width:216px;height:204px}

/* footer */
.footer{top:4832px;height:312px;background:var(--footer);color:#fff}
.f-col{top:72px}
.f-col h5{font-family:"Montserrat",sans-serif;font-weight:600;font-size:18px;margin-bottom:22px;letter-spacing:.5px}
.f-col ul{list-style:none;font-size:13px;line-height:18.5px}
.f-col li::before{content:"\25BA";font-size:9px;margin-right:10px}
.f-col p{font-size:13px;line-height:18.5px;margin-bottom:14px}
.f-div{top:58px;width:1px;height:190px;background:rgba(255,255,255,.5)}
.f-input{width:218px;height:32px;background:#fff;color:#333;font-size:11.5px;padding-left:14px;line-height:32px;margin-bottom:12px}
.f-btn{width:114px;height:20px;border-radius:10px;background:var(--brand-green);font-size:11px;font-family:"Montserrat",sans-serif;font-weight:600;line-height:20px;padding-left:16px}
.copyright{top:5144px;height:46px;background:var(--footer-bar);color:#ddd;font-size:12px;text-align:center;line-height:46px}
</style>
</head>
<body>

<header class="section header">
  <div class="abs brand"><span class="brand-dot"></span><span class="brand-name">Velvet Paws Cat Sitting</span></div>
  <div class="abs call">Call Us<strong>012-555-0147</strong></div>
  <div class="abs follow">Follow Us<div class="social"><span></span><span></span><span></span><span></span></div></div>
</header>

<nav class="section nav">
  <a href="#">HOME</a><a href="#">ABOUT</a><a href="#">SERVICES</a><a href="#">GALLERY</a><a href="#">PRICING</a><a href="#">FAQ</a><a href="#">CONTACT US</a>
</nav>

<section class="section hero" role="img" aria-label="Photo of a smiling woman lifting a grey and white kitten">
  <h1 class="abs hero-title">SPECIAL CARE</h1>
  <div class="abs hero-sub">For your cats</div>
  <p class="abs hero-copy">Lorem ipsum dolor sit amet, consectetur adipiscing elit, sed do eiusmod tempor incididunt ut labore et dolore magna aliqua. Ut enim ad minim veniam, quis nostrud exercitation</p>
  <div class="abs btn-green hero-btn">
    <svg width="18" height="18" viewBox="0 0 20 20"><g fill="#fff"><ellipse cx="10" cy="13.5" rx="5" ry="4.2"/><circle cx="4" cy="8" r="2.2"/><circle cx="8" cy="4.5" r="2.2"/><circle cx="12.5" cy="4.5" r="2.2"/><circle cx="16.3" cy="8" r="2.2"/></g></svg>
    Make An Appointment
  </div>
</section>

<section class="section about">
  <div class="abs about-photo" role="img" aria-label="Photo of an older woman holding a white cat on a sofa"></div>
  <h2 class="abs h-green about-title">About Us</h2>
  <div class="abs rule about-rule"></div>
  <div class="abs about-text">
    <p>Verum tamen cum de rebus grandioribus dicas, ipsae res verba rapiunt; Hoc non est positum in nostra actione. Quod ea non occurrentia fingunt, vincunt Aristonem; Haec para/doca illi, nos admirabilia dicamus. Et quidem, inquit, vehementer errat; Quarum ambarum rerum cum medicinam pollicetur, luxuriae licentiam</p>
    <p>pollicetur. Laelius clamores sofòw ille so lebat Edere compellans gumias ex ordine nostros.Verum tamen cum de rebus grandioribus dicas, ipsae res verba rapiunt; Hoc non est positum in nostra actione.</p>
    <p>Quod ea non occurrentia fingunt, vincunt Aristonem; Haec para/doca illi, nos admirabilia dicamus. Et quidem, inquit, vehementer errat; Quarum ambarum rerum cum medicinam pollicetur, luxuriae licentiam</p>
  </div>
  <div class="abs pill about-more">READ MORE <i></i></div>
</section>

<section class="section services">
  <h2 class="abs services-title">Our <b>Services</b></h2>
  <div class="abs rule services-rule"></div>
  <div class="abs service" style="left:83px">
    <div class="service-photo" role="img" aria-label="Photo of a cat being brushed"></div>
    <h3>Wellness<span>care</span></h3>
    <p>Honesto quic quam honestius<br>nec turpi turpius. Tria genera bonorum<br>honestius nec turpi turpius.</p>
    <div class="pill">READ MORE <i></i></div>
  </div>
  <div class="abs service" style="left:443px">
    <div class="service-photo" role="img" aria-label="Photo of a ginger and white cat at a vet check"></div>
    <h3>Nutritional<span>Counseling</span></h3>
    <p>Honesto quic quam honestius<br>nec turpi turpius. Tria genera bonorum<br>honestius nec turpi turpius.</p>
    <div class="pill">READ MORE <i></i></div>
  </div>
  <div class="abs service" style="left:784px">
    <div class="service-photo" role="img" aria-label="Photo of a vet listening to a cat with a stethoscope"></div>
    <h3>Vaccination<span>Care</span></h3>
    <p>Honesto quic quam honestius<br>nec turpi turpius. Tria genera bonorum<br>honestius nec turpi turpius.</p>
    <div class="pill">READ MORE <i></i></div>
  </div>
</section>

<section class="section faq">
  <h2 class="abs faq-title">FAQ'S</h2>
  <div class="abs faq-item" style="top:160px;border-bottom:none">
    <div class="faq-q"><span>Est enim effectrix multarum et magnarum voluptatum</span><span>&#8211;</span></div>
    <p class="faq-a">Grandioribus dicas, ipsae res verba rapiunt; Hoc non est positum in nostra actione. Quod ea non occurrentia fingunt, vincunt Aristonem; Haec para/doca illi, nos admirabilia dicamus. Et quidem, inquit, vehementer errat; Quarum ambarum rerum .</p>
  </div>
  <div class="abs faq-item" style="top:280px;height:50px"><div class="faq-q"><span>Est enim effectrix multarum et ?</span><span>+</span></div></div>
  <div class="abs faq-item" style="top:368px;height:52px"><div class="faq-q"><span>Est enim effectrix multarum et ?</span><span>+</span></div></div>
  <div class="abs faq-item" style="top:456px;height:56px"><div class="faq-q"><span>Est enim effectrix multarum et ?</span><span>+</span></div></div>
</section>

<section class="section rates">
  <h2 class="abs rates-title">My <b>Rates</b></h2>
  <p class="abs rates-copy">Grandioribus dicas, ipsae res verba rapiunt; Hoc non est positum in nostra actione. Quod ea non occurrentia fingunt, vincunt Aristonem; Haec para/doca illi, nos admirabilia dicamus. Et quidem, inquit, vehementer errat; Quarum ambarum rerum .Honesto quic quam honestius nec turpi turpius. Tria genera bonorumhonestius nec turpi turpius.</p>
  <div class="abs plan" style="left:222px;top:267px">
    <div class="plan-head">Basic</div>
    <div class="plan-price">90<sup>$</sup></div>
    <div class="plan-tag">Huic mori opti<br>sse propter desper</div>
    <ul><li>&#10003; Neque solum ea</li><li>&#10003; Communia, verum</li><li>&#10003; Etiam paria esse</li><li>&#10003; Dixerunt.</li></ul>
    <div class="pill">SELECT <i></i></div>
  </div>
  <div class="abs plan" style="left:508px;top:260px">
    <div class="plan-head">Gold</div>
    <div class="plan-price">90<sup>$</sup></div>
    <div class="plan-tag">Huic mori opti<br>sse propter desper</div>
    <ul><li>&#10003; Neque solum ea</li><li>&#10003; Communia, verum</li><li>&#10003; Etiam paria esse</li><li>&#10003; Dixerunt.</li></ul>
    <div class="pill">SELECT <i></i></div>
  </div>
  <div class="abs plan" style="left:802px;top:258px">
    <div class="plan-head">Premium</div>
    <div class="plan-price">90<sup>$</sup></div>
    <div class="plan-tag">Huic mori opti<br>sse propter desper</div>
    <ul><li>&#10003; Neque solum ea</li><li>&#10003; Communia, verum</li><li>&#10003; Etiam paria esse</li><li>&#10003; Dixerunt.</li></ul>
    <div class="pill">SELECT <i></i></div>
  </div>
</section>

<section class="section testimonials">
  <h2 class="abs t-title">Testimonials</h2>
  <div class="abs rule t-rule"></div>
  <svg class="abs" style="left:140px;top:252px" width="24" height="40" viewBox="0 0 24 40"><path d="M20 4 6 20l14 16" fill="none" stroke="#888" stroke-width="3"/></svg>
  <svg class="abs" style="left:1036px;top:252px" width="24" height="40" viewBox="0 0 24 40"><path d="M4 4l14 16L4 36" fill="none" stroke="#888" stroke-width="3"/></svg>
  <div class="abs quote" style="left:228px">
    <div class="quote-mark">&#8220;</div>
    <h4>Highly Professional Team</h4>
    <p>Abent ipsum dolor sit amet, consectetur adipiscing elit. Quid autem habent admirationis, cum prope accesseris An hoc usque quaque, aliter in vita</p>
    <div class="who">ELIAS MORROW</div>
    <div class="role">Manager</div>
  </div>
  <div class="abs quote" style="left:666px">
    <div class="quote-mark">&#8220;</div>
    <h4>Highly Professional Team</h4>
    <p>Mirationis ipsum dolor sit amet, consectetur adipiscing elit. Quid autem habent admirationis, cum prope accesseris An hoc usque quaque, aliter in vita</p>
    <div class="who">GRANT HOLLOWAY</div>
    <div class="role">Top Manager</div>
  </div>
</section>

<section class="section signup">
  <div class="abs signup-icon">
    <svg width="40" height="40" viewBox="0 0 40 40"><rect x="10" y="13" width="20" height="14" fill="none" stroke="#fff" stroke-width="2"/><path d="M10 13l10 8 10-8" fill="none" stroke="#fff" stroke-width="2"/></svg>
  </div>
  <div class="abs signup-label">News letter Signup</div>
  <div class="abs signup-input">Enter Your Email</div>
  <div class="abs signup-btn">SUBSCRIBE</div>
</section>

<section class="section gallery">
  <h2 class="abs g-title">
    <svg width="30" height="30" viewBox="0 0 20 20" style="vertical-align:-4px;margin-right:6px"><g fill="#7dbb42"><ellipse cx="10" cy="13.5" rx="5" ry="4.2"/><circle cx="4" cy="8" r="2.2"/><circle cx="8" cy="4.5" r="2.2"/><circle cx="12.5" cy="4.5" r="2.2"/><circle cx="16.3" cy="8" r="2.2"/></g></svg>Gallery</h2>
  <div class="abs rule g-rule"></div>
  <div class="abs g-photo" style="left:139px;top:204px;background:linear-gradient(135deg,#8a6a55,#c9a78a)" role="img" aria-label="Photo of a couple cuddling a cat"></div>
  <div class="abs g-photo" style="left:375px;top:204px;background:linear-gradient(135deg,#6d6f78,#c3b2a3)" role="img" aria-label="Photo of a smiling couple holding a tabby cat"></div>
  <div class="abs g-photo" style="left:610px;top:204px;background:linear-gradient(135deg,#a99a8b,#6f6258)" role="img" aria-label="Photo of a woman relaxing with her cat"></div>
  <div class="abs g-photo" style="left:846px;top:204px;background:linear-gradient(135deg,#9fb3c9,#d9c09a)" role="img" aria-label="Photo of a vet holding a small dog"></div>
  <div class="abs g-photo" style="left:139px;top:428px;background:linear-gradient(135deg,#d6a54d,#7a5a2e)" role="img" aria-label="Photo of two cats in a sunny garden"></div>
  <div class="abs g-photo" style="left:375px;top:428px;background:linear-gradient(135deg,#f2f0ec,#c99a6a)" role="img" aria-label="Photo of a woman with a kitten and a puppy"></div>
  <div class="abs g-photo" style="left:610px;top:428px;background:linear-gradient(135deg,#5f7c95,#a9bacb)" role="img" aria-label="Photo of a kitten and a dog together"></div>
  <div class="abs g-photo" style="left:846px;top:428px;background:linear-gradient(135deg,#e9e1d8,#c28e66)" role="img" aria-label="Photo of a ginger kitten held up close"></div>
</section>

<footer class="section footer">
  <div class="abs f-col" style="left:139px"><h5>QUICK LINK</h5>
    <ul><li>Home</li><li>About</li><li>Services</li><li>gallery</li><li>Pricing</li><li>Faq</li><li>Contact US</li></ul></div>
  <div class="abs f-div" style="left:326px"></div>
  <div class="abs f-col" style="left:367px"><h5>CONTACT INFO</h5>
    <p>4120 Maple Crest Road<br>Juneau,<br>Alaska 34512</p>
    <p>369-555-0192<br>info@velvetpaws.com<br>www.velvetpaws.com</p></div>
  <div class="abs f-div" style="left:582px"></div>
  <div class="abs f-col" style="left:629px"><h5>TIME HOURS</h5>
    <p>M-F : 8am - 7pm<br>Sat : 8am - 5am<br>Sun : Noon - 5pm</p>
    <p>Contact Us<br>For holiday hours</p></div>
  <div class="abs f-div" style="left:806px"></div>
  <div class="abs f-col" style="left:864px"><h5>NEWSLETTER</h5>
    <div class="f-input">Your Name</div>
    <div class="f-input">Your Email</div>
    <div class="f-btn">SIGN UP</div></div>
</footer>

<div class="section copyright">Copyright 2022, velvetpaws, All Right Reserved</div>

</body>
</html>
```